Two (2) Merchant Advance Banner Ads

I need two (2) ads with rotating gif with 3 transitions for http://lendorbit.com/

Ad Specs:
Ad 1 must be an image equal to 250x250 pixels for website and email newsletter. .jpg, .gif, and
.png okay. No Flash!

Ad 2 must be an image equal to 720x90 pixels for website and mobile device view. .jpg, .gif, and
.png only. No Flash!

Client: Marlowe Funding Partners merchant cash advance company out of Chicago. They provide alternative (to a bank loan) financing for small business owners across the U.S.
Here's their website: www.marlowefp.com

Purpose: Recruit 3rd party sellers of alternative financing. There are many sales financing professionals already out there soliciting small businesses, we want them to make a decision to sell Marlowe's financing product to small businesses.

Copy:
Real People.
Competitive Commissions.
Great Rates.

I would like the logo (attached), phone number and CTA button to appear on all three transitions.
Call (888) 471-2859
Button: Get Started

Style:
Either something clean and simple, or something similar (not identifcal) to ads attached.
Brand standards guide is attached. Please use colors from guide.

```html
<!DOCTYPE html>
<html lang="en">
<head>
<meta charset="utf-8">
<title>Marlowe Funding Partners – Partner Banner Frames</title>
<link rel="stylesheet" href="https://fonts.googleapis.com/css2?family=Montserrat:wght@300;400;600;700;800&display=swap">
<style>
  :root{
    --stage:#000000;
    --lime:#b3c634;
    --lime-light:#d6e06a;
    --lime-dark:#9fb52c;
    --ink:#4b4f6a;
    --green-text:#8cb53a;
    --bubble:#f1f1f1;
    --teal:#1a9aa8;
    --teal-dark:#147f8b;
    --white:#ffffff;
    --figure-a:#e9ecef;
    --figure-b:#c99a72;
  }
  *{box-sizing:border-box;margin:0;padding:0}
  html,body{width:1200px;height:525px;overflow:hidden;background:var(--stage)}
  body{font-family:"Montserrat",Arial,sans-serif;position:relative}

  .banner{
    position:absolute;left:55px;width:1078px;height:134px;overflow:hidden;
    background:radial-gradient(ellipse 55% 120% at 62% 50%,var(--lime-light) 0%,var(--lime) 55%,var(--lime-dark) 100%);
  }
  .banner--one{top:55px}
  .banner--two{top:197px}
  .banner--three{top:340px}

  .brand-panel{position:absolute;left:0;top:0;width:300px;height:134px}
  .brand-name{
    position:absolute;left:26px;top:38px;width:230px;
    font-weight:600;font-size:25px;line-height:1.12;color:var(--ink);
  }

  .figure-slot{
    position:absolute;left:292px;top:9px;width:140px;height:125px;
    border-radius:62px 62px 0 0;
    background:linear-gradient(180deg,var(--figure-b) 0%,var(--figure-a) 55%,var(--figure-a) 100%);
  }

  .bubble{
    position:absolute;left:456px;top:16px;width:335px;height:97px;
    background:var(--bubble);border-radius:14px;
    box-shadow:2px 4px 6px rgba(0,0,0,.25);
    display:flex;flex-direction:column;align-items:center;justify-content:center;
    text-align:center;
  }
  .bubble::before{
    content:"";position:absolute;left:-16px;top:38px;
    border-top:10px solid transparent;border-bottom:10px solid transparent;
    border-right:17px solid var(--bubble);
  }
  .headline{font-size:40px;letter-spacing:.3px;color:var(--green-text);line-height:1;white-space:nowrap}
  .headline strong{font-weight:800}
  .headline span{font-weight:300}
  .headline--stack{color:var(--ink);display:flex;flex-direction:column;align-items:center}
  .headline--stack strong{font-size:34px;line-height:1}
  .headline--stack span{font-size:31px;line-height:1.05}

  .contact{
    position:absolute;left:818px;top:10px;width:240px;
    display:flex;flex-direction:column;align-items:center;color:var(--white);
  }
  .contact-label{font-weight:700;font-size:20px;letter-spacing:5px;line-height:1}
  .contact-phone{font-weight:600;font-size:27px;line-height:1.2;margin-top:2px;white-space:nowrap}
  .cta{
    margin-top:7px;width:222px;height:44px;border-radius:9px;
    background:var(--teal);box-shadow:0 3px 0 var(--teal-dark),2px 4px 6px rgba(0,0,0,.25);
    display:flex;align-items:center;justify-content:center;
    font-weight:700;font-size:25px;color:var(--white);letter-spacing:.3px;
  }
</style>
</head>
<body>

<section class="banner banner--one">
  <svg class="brand-panel" viewBox="0 0 300 134" aria-hidden="true">
    <path d="M0 0 H170 C235 20 262 80 256 134 H0 Z" fill="#ffffff"/>
  </svg>
  <p class="brand-name">Marlowe Funding Partners</p>
  <div class="figure-slot" role="img" aria-label="Illustrated salesman in glasses and tie holding up one finger"></div>
  <div class="bubble"><p class="headline"><strong>REAL</strong> <span>PEOPLE.</span></p></div>
  <div class="contact">
    <span class="contact-label">CALL</span>
    <span class="contact-phone">(888) 471-2859</span>
    <span class="cta">GET STARTED</span>
  </div>
</section>

<section class="banner banner--two">
  <svg class="brand-panel" viewBox="0 0 300 134" aria-hidden="true">
    <path d="M0 0 H170 C235 20 262 80 256 134 H0 Z" fill="#ffffff"/>
  </svg>
  <p class="brand-name">Marlowe Funding Partners</p>
  <div class="figure-slot" role="img" aria-label="Illustrated salesman in glasses and tie holding up two fingers"></div>
  <div class="bubble"><p class="headline headline--stack"><strong>COMPETITIVE</strong><span>COMMISSIONS.</span></p></div>
  <div class="contact">
    <span class="contact-label">CALL</span>
    <span class="contact-phone">(888) 471-2859</span>
    <span class="cta">GET STARTED</span>
  </div>
</section>

<section class="banner banner--three">
  <svg class="brand-panel" viewBox="0 0 300 134" aria-hidden="true">
    <path d="M0 0 H170 C235 20 262 80 256 134 H0 Z" fill="#ffffff"/>
  </svg>
  <p class="brand-name">Marlowe Funding Partners</p>
  <div class="figure-slot" role="img" aria-label="Illustrated salesman in glasses and tie holding up three fingers"></div>
  <div class="bubble"><p class="headline"><strong>GREAT</strong> <span>RATES.</span></p></div>
  <div class="contact">
    <span class="contact-label">CALL</span>
    <span class="contact-phone">(888) 471-2859</span>
    <span class="cta">GET STARTED</span>
  </div>
</section>

</body>
</html>
```